Apartment Investor Business Card Design

Need a new business card designed for my multifamily investment company

Industry/Entity Type

Real Estate

Contact Information for Business Card

Marlow Pickett - President & CEO
Brightfield Capital, LLC
4870 North 52nd Avenue, Ste 150
Omaha, NE 68231
(402) 555-0193
Marlow@brightfieldcapitalmidwest.example
Www.BrightfieldCapitalMidwest.example

Colors
3176b5

```html
<!DOCTYPE html>
<html lang="en">
<head>
<meta charset="utf-8">
<title>Brightfield Capital – Business Card</title>
<link rel="stylesheet" href="https://fonts.googleapis.com/css2?family=Roboto:wght@400;500;700&display=swap">
<style>
  :root {
    --brand-blue: #3176b5;
    --band-blue: #4f86c6;
    --band-gray: #9a9a9a;
    --ink: #2b2b2b;
    --ink-soft: #555555;
    --card-black: #1e1f21;
    --mark-gray: #3a3b3d;
    --paper: #ffffff;
    --stage: #4a4b4d;
  }
  * { margin: 0; padding: 0; box-sizing: border-box; }
  html, body {
    width: 1200px; height: 1000px; overflow: hidden;
    background: var(--stage);
    font-family: "Roboto", Arial, sans-serif;
  }
  .card {
    position: absolute;
    left: 200px;
    width: 800px; height: 457px;
    border-radius: 30px;
    overflow: hidden;
  }
  /* Back side */
  .card-back {
    top: 28px;
    background: var(--card-black);
  }
  .card-back .brand-name {
    position: absolute; left: 0; right: 0; top: 170px;
    text-align: center;
    font-size: 52px; font-weight: 400; letter-spacing: 4px;
    color: var(--mark-gray);
    text-transform: uppercase;
  }
  .card-back .brand-square {
    display: block; width: 22px; height: 22px;
    margin: 0 auto 18px; background: var(--mark-gray);
    position: absolute; left: 389px; top: 130px;
  }
  .card-back .site {
    position: absolute; left: 0; right: 0; top: 372px;
    text-align: center; font-size: 15px; color: var(--paper);
  }
  .site .accent { color: var(--band-blue); }

  /* Front side */
  .card-front {
    top: 515px;
    background: var(--paper);
  }
  .card-front .bands { position: absolute; inset: 0; }
  .front-brand {
    position: absolute; left: 40px; top: 150px; width: 380px;
    text-align: center;
  }
  .front-brand .brand-square {
    display: block; width: 20px; height: 20px; margin: 0 auto 14px;
    background: var(--ink);
  }
  .front-brand .brand-name {
    font-size: 34px; font-weight: 400; letter-spacing: 2px;
    color: var(--ink); text-transform: uppercase;
  }
  .divider {
    position: absolute; left: 440px; top: 140px;
    width: 1px; height: 190px; background: #9c9c9c;
  }
  .contact {
    position: absolute; left: 462px; top: 138px; right: 16px;
    color: var(--ink-soft); font-size: 14.5px; line-height: 1.3;
  }
  .contact .person {
    font-size: 21px; font-weight: 700; color: var(--brand-blue);
    text-transform: uppercase; letter-spacing: .3px;
  }
  .contact .role { font-size: 14px; margin-bottom: 12px; }
  .contact .company { font-weight: 700; color: var(--brand-blue); }
  .contact .address { margin-bottom: 6px; }
  .contact .line { display: flex; align-items: center; gap: 8px; }
  .contact .line svg { width: 13px; height: 13px; flex: none; fill: var(--brand-blue); }
</style>
</head>
<body>

<section class="card card-back" aria-label="Card back">
  <span class="brand-square"></span>
  <div class="brand-name">Brightfield Capital</div>
  <div class="site">www.<span class="accent">BrightfieldCapitalMidwest</span>.example</div>
</section>

<section class="card card-front" aria-label="Card front">
  <svg class="bands" viewBox="0 0 800 457" preserveAspectRatio="none" aria-hidden="true">
    <path d="M0,262 C160,330 360,362 540,378 C660,388 750,402 800,420 L800,457 L0,457 Z" fill="var(--band-gray)"/>
    <path d="M0,280 C160,345 360,372 540,388 C660,398 750,412 800,428 L800,457 L0,457 Z" fill="var(--paper)"/>
    <path d="M0,292 C160,358 360,384 540,398 C660,408 750,420 800,434 L800,457 L0,457 Z" fill="var(--band-blue)"/>
  </svg>

  <div class="front-brand">
    <span class="brand-square"></span>
    <div class="brand-name">Brightfield Capital</div>
  </div>

  <div class="divider"></div>

  <div class="contact">
    <div class="person">Marlow Pickett</div>
    <div class="role">President &amp; CEO</div>
    <div class="company">Brightfield Capital, LLC</div>
    <div class="address">4870 North 52nd Avenue, Ste 150<br>Omaha, NE 68231</div>
    <div class="line">
      <svg viewBox="0 0 24 24"><path d="M6.6 10.8a15.1 15.1 0 0 0 6.6 6.6l2.2-2.2a1 1 0 0 1 1-.25 11.4 11.4 0 0 0 3.6.57 1 1 0 0 1 1 1V20a1 1 0 0 1-1 1A17 17 0 0 1 3 4a1 1 0 0 1 1-1h3.5a1 1 0 0 1 1 1c0 1.25.2 2.45.57 3.57a1 1 0 0 1-.25 1z"/></svg>
      <span>(402) 555-0193</span>
    </div>
    <div class="line">
      <svg viewBox="0 0 24 24"><path d="M2 5h20v14H2z M4 7v.5l8 5 8-5V7l-8 5z" fill-rule="evenodd"/></svg>
      <span>Marlow@brightfieldcapitalmidwest.example</span>
    </div>
    <div class="line">
      <svg viewBox="0 0 24 24"><path d="M12 2a10 10 0 1 0 0 20 10 10 0 0 0 0-20zm6.9 6h-3a15 15 0 0 0-1.4-3.9A8 8 0 0 1 18.9 8zM12 4a13 13 0 0 1 1.9 4h-3.8A13 13 0 0 1 12 4zM4.3 14a8 8 0 0 1 0-4h3.4a16 16 0 0 0 0 4zm.8 2h3a15 15 0 0 0 1.4 3.9A8 8 0 0 1 5.1 16zm3-8h-3a8 8 0 0 1 4.4-3.9A15 15 0 0 0 8.1 8zM12 20a13 13 0 0 1-1.9-4h3.8A13 13 0 0 1 12 20zm2.3-6H9.7a14 14 0 0 1 0-4h4.6a14 14 0 0 1 0 4zm.2 5.9a15 15 0 0 0 1.4-3.9h3a8 8 0 0 1-4.4 3.9zM16.3 14a16 16 0 0 0 0-4h3.4a8 8 0 0 1 0 4z"/></svg>
      <span>www.<span style="color:var(--brand-blue)">BrightfieldCapitalMidwest</span>.example</span>
    </div>
  </div>
</section>

</body>
</html>
```